Business Card Design

We need a business card design for a new company based in Allen, Texas. (outside of Dallas,Texas) We offer Business Management Solutions to Entrepreneurs, as well as Corporate Businesses. Our product line offers solutions to Image, Branding, Social Media marketing, business development strategies, banking / funding solutions, just to name a few. We would like to see designs that convey strength and confidence. I have attached a sample design of our company name. Designers you may use company name as either: Vorlix or Vorlix Corporation, depending on the design layout.

Please show alternate color of Black as well.

Industry/Entity Type

Business

Contact Information for Business Card

Vorlix Corporation

2847 E. Hollowbrook Drive, STE 410
Allen, TX 75013
Office: 469.318.7742
Fax: 469.318.7743

Dr. Miles Dunworth
Business Development Director

```html
<!DOCTYPE html>
<html lang="en">
<head>
<meta charset="utf-8">
<title>Vorlix Corporation — Business Card</title>
<link rel="stylesheet" href="https://fonts.googleapis.com/css2?family=Montserrat:wght@300;400;500&display=swap">
<style>
  :root {
    --canvas: #e9e7e4;
    --card-black: #0c0c0c;
    --card-white: #ffffff;
    --ink: #1a1a1a;
    --rule-light: #ffffff;
    --rule-dark: #111111;
    --silver: #c9c9c9;
    --muted-white: #e6e6e6;
  }
  * { box-sizing: border-box; margin: 0; padding: 0; }
  html, body { width: 1200px; height: 900px; overflow: hidden; }
  body {
    background: var(--canvas);
    font-family: "Montserrat", Arial, sans-serif;
    position: relative;
  }
  .card {
    position: absolute;
    width: 560px;
    height: 320px;
    border-radius: 22px;
    overflow: hidden;
    box-shadow: 0 14px 30px rgba(0,0,0,.18);
  }
  /* Front */
  .card-front {
    left: 320px; top: 70px;
    background: linear-gradient(135deg, #262626 0%, var(--card-black) 45%, #050505 100%);
    color: var(--rule-light);
  }
  .front-rule-top {
    position: absolute; left: 0; right: 0; top: 64px;
    height: 3px; background: var(--rule-light);
  }
  .front-name {
    position: absolute; left: 0; right: 0; top: 98px;
    text-align: center;
    font-size: 76px; font-weight: 300; letter-spacing: 2px;
    color: var(--rule-light);
    line-height: 1;
  }
  .front-tagline {
    position: absolute; left: 0; right: 0; top: 222px;
    display: flex; align-items: center; gap: 14px;
  }
  .front-tagline .rule { height: 3px; background: var(--rule-light); }
  .front-tagline .rule-left { width: 150px; }
  .front-tagline .rule-right { flex: 1; }
  .front-tagline .label {
    font-size: 22px; font-weight: 300; color: var(--muted-white); letter-spacing: .5px;
  }
  /* Back */
  .card-back {
    left: 320px; top: 470px;
    background: var(--card-white);
    color: var(--ink);
  }
  .back-rule {
    position: absolute; left: 0; right: 0; top: 46px;
    height: 3px; background: var(--rule-dark);
  }
  .back-address {
    position: absolute; left: 30px; right: 26px; top: 62px;
    font-size: 15px; font-weight: 400; text-align: right; letter-spacing: .2px;
  }
  .back-contacts {
    position: absolute; right: 30px; top: 108px;
    list-style: none; display: flex; flex-direction: column; gap: 12px;
  }
  .back-contacts li {
    display: flex; align-items: center; gap: 12px;
    font-size: 17px; font-weight: 400;
  }
  .back-contacts svg { width: 26px; height: 26px; }
  .back-name {
    position: absolute; left: 40px; bottom: 28px;
    font-size: 92px; font-weight: 300; color: var(--silver);
    letter-spacing: 2px; line-height: 1;
  }
</style>
</head>
<body>
  <section class="card card-front" aria-label="Card front">
    <div class="front-rule-top"></div>
    <div class="front-name">Vorlix</div>
    <div class="front-tagline">
      <span class="rule rule-left"></span>
      <span class="label">Corporation</span>
      <span class="rule rule-right"></span>
    </div>
  </section>

  <section class="card card-back" aria-label="Card back">
    <div class="back-rule"></div>
    <p class="back-address">2847 E. Hollowbrook Drive, STE 410 Allen, TX 75013</p>
    <ul class="back-contacts">
      <li>
        <svg viewBox="0 0 26 26" aria-label="Office phone">
          <path d="M3 9c0-3 4-5 10-5s10 2 10 5v2h-5V8.5c-1.5-.6-3-.8-5-.8s-3.5.2-5 .8V11H3z" fill="#111"/>
          <path d="M7 12h12l3 10H4z" fill="#111"/>
          <circle cx="13" cy="17" r="2.6" fill="#fff"/>
        </svg>
        <span>469.318.7742</span>
      </li>
      <li>
        <svg viewBox="0 0 26 26" aria-label="Fax">
          <rect x="7" y="2" width="12" height="10" fill="none" stroke="#111" stroke-width="1.6"/>
          <line x1="9.5" y1="5.5" x2="16.5" y2="5.5" stroke="#111" stroke-width="1.2"/>
          <line x1="9.5" y1="8.5" x2="16.5" y2="8.5" stroke="#111" stroke-width="1.2"/>
          <rect x="3" y="12" width="20" height="12" rx="1.5" fill="#111"/>
          <rect x="6" y="15" width="9" height="2" fill="#fff"/>
          <rect x="17" y="15" width="3" height="6" fill="#fff"/>
        </svg>
        <span>469.318.7743</span>
      </li>
    </ul>
    <div class="back-name">Vorlix</div>
  </section>
</body>
</html>
```